Willow of Meadow Uniform Label Redesign

To refine our current product label designs into one, simple, modern, crisp, general look that can be adapted to all our all Natural Skin Care and Wellness products. I am inspired by the elegant versatility of products like Lumavel Botanic Beauty or Tarn Beauty label schemes. We no longer want labels that indicate scent or ingredients. We have two primary colors that we want to maintain (#096CA3 and #DEE33F), and are willing to entertain subtle additions of others, other than black. Our labels will be printed on white or clear material. We use mainly Cosmo or Boston Round container shapes, plus flat top, smooth, round jars. Maybe a faded watermark highlight the "natural" or "beautiful" side of our products. we need to convey confidence, while remaining simple. We currently use the Advantage font. Maybe Century Gothic may work. Something similar that is easy on the eyes. Maybe vertical main text? We are willing to entertain a lot of ideas. These designs will offer ideas into our eventual Website (www.willowofmeadow-example.com) redesign.

Target Market(s)

Those who are familiar with the power of natural, plant based skin care and wellness products

Industry/Entity Type

Natural Skin Care and Wellness

Font styles to use
Sans Serif
Other font styles liked:
• Century Gothic, Advantage, or similar that is easy on the eyes

Colors
0054AA
0677BA
7BADD7
CADEEF
E8F1F8
59FF00
82FF00
B8FF75
E3FFCB
F4FFEA

Requirements
Must have
• "Clean Lines"; These colors: (#096CA3 and #DEE33F)
Nice to have
• MAYBE vertical main text or a watermark image

```html
<!DOCTYPE html>
<html lang="en">
<head>
<meta charset="UTF-8">
<title>Willow of Meadow – Uniform Label</title>
<link rel="stylesheet" href="https://fonts.googleapis.com/css2?family=Oswald:wght@500&family=Roboto+Condensed:wght@400;500&display=swap">
<style>
  :root {
    --page-bg: #f4f4f4;
    --label-blue: #1a6c9c;
    --label-blue-light: #2c80b0;
    --label-blue-dark: #14587f;
    --brand-yellow: #e4e81f;
    --text-white: #ffffff;
    --text-soft: #e6eef4;
  }
  * { margin: 0; padding: 0; box-sizing: border-box; }
  html, body {
    width: 1200px;
    height: 800px;
    overflow: hidden;
    background: var(--page-bg);
  }
  .canvas {
    position: relative;
    width: 1200px;
    height: 800px;
  }
  .label {
    position: absolute;
    left: 370px;
    top: 40px;
    width: 460px;
    height: 720px;
    background: var(--label-blue);
    border-radius: 6px;
    overflow: hidden;
  }
  .label-watermark {
    position: absolute;
    inset: 0;
    background: linear-gradient(100deg, var(--label-blue-dark) 0%, var(--label-blue-light) 45%, var(--label-blue) 70%, var(--label-blue-dark) 100%);
    opacity: 0.9;
  }
  .brand {
    position: absolute;
    top: 150px;
    left: 0;
    width: 100%;
    text-align: center;
  }
  .brand-name {
    font-family: "Roboto Condensed", sans-serif;
    font-weight: 400;
    font-size: 44px;
    line-height: 1.1;
    color: var(--text-white);
  }
  .brand-tagline {
    margin-top: 10px;
    font-family: "Roboto Condensed", sans-serif;
    font-weight: 500;
    font-size: 15px;
    letter-spacing: 3px;
    color: var(--brand-yellow);
  }
  .product {
    position: absolute;
    left: 78px;
    top: 370px;
  }
  .product-name {
    font-family: "Oswald", sans-serif;
    font-weight: 500;
    font-size: 54px;
    line-height: 1;
    color: var(--brand-yellow);
    letter-spacing: -0.5px;
  }
  .product-details {
    margin-top: 16px;
    padding-left: 18px;
    border-left: 5px solid var(--brand-yellow);
  }
  .detail + .detail { margin-top: 16px; }
  .detail-title {
    font-family: "Roboto Condensed", sans-serif;
    font-weight: 500;
    font-size: 34px;
    line-height: 1.1;
    color: var(--text-soft);
  }
  .detail-sub {
    font-family: "Roboto Condensed", sans-serif;
    font-weight: 400;
    font-size: 30px;
    line-height: 1.15;
    color: var(--text-soft);
  }
  .volume {
    position: absolute;
    bottom: 46px;
    left: 0;
    width: 100%;
    text-align: center;
    font-family: "Roboto Condensed", sans-serif;
    font-size: 28px;
    color: var(--text-white);
  }
</style>
</head>
<body>
  <main class="canvas">
    <section class="label">
      <div class="label-watermark" role="img" aria-label="Faint interlocking circle watermark pattern across the blue label"></div>

      <header class="brand">
        <h1 class="brand-name">Willow of Meadow</h1>
        <p class="brand-tagline">PURE. GENTLE. EVERY DAY.</p>
      </header>

      <div class="product">
        <h2 class="product-name">PRODUCT NAME</h2>
        <div class="product-details">
          <div class="detail">
            <p class="detail-title">LOREM IPSUM</p>
            <p class="detail-sub">Subtext Here</p>
          </div>
          <div class="detail">
            <p class="detail-title">LOREM IPSUM</p>
            <p class="detail-sub">Subtext Here</p>
          </div>
        </div>
      </div>

      <p class="volume">9fl. oz (99 ml)</p>
    </section>
  </main>
</body>
</html>
```